GLOW ON THE AVENUE WEBSITE

I have a website www.glowontheavenue.org , need information from that jazzed up. wanted page to be fun & funky .

Target Market(s)

18 to 35yrs guys & girls

Requirements
Must have
• use all photos on website, need to attached my brochure for printing

```html
<!DOCTYPE html>
<html lang="en">
<head>
<meta charset="utf-8">
<title>Glow on the Avenue</title>
<link rel="stylesheet" href="https://fonts.googleapis.com/css2?family=Questrial&family=Varela+Round&display=swap">
<style>
:root{
  --red:#c70000;
  --red-deep:#9a0000;
  --red-shade:#a80000;
  --black:#0b0406;
  --white:#ffffff;
  --yellow:#f2e024;
  --orange:#f0a35a;
  --ink:#111111;
}
*{margin:0;padding:0;box-sizing:border-box}
html,body{width:858px;height:1200px;overflow:hidden;background:var(--red)}
body{position:relative;font-family:"Questrial",sans-serif;color:var(--ink)}
.abs{position:absolute;white-space:nowrap}

.hero{left:0;top:0;width:858px;height:278px;
  background:linear-gradient(100deg,#2a2426 0%,#3b2f31 25%,#7a1010 45%,#c21313 65%,#3a3334 85%,#1f1a1b 100%)}
.hero-band{left:0;top:278px;width:858px;height:15px;background:var(--black)}

.brand-tab{left:58px;top:226px;width:160px;height:67px;background:var(--white);border-radius:8px 8px 0 0;
  display:flex;align-items:center;justify-content:center;text-align:center}
.brand-name{font-family:"Varela Round",sans-serif;color:var(--red);font-size:18px;line-height:20px}

.side-shadow{left:8px;top:293px;width:258px;height:492px;background:var(--red-shade);border-radius:0 0 8px 8px}
.side-panel{left:17px;top:293px;width:240px;height:484px;background:var(--white);border-radius:0 0 8px 8px}
.side-nav{left:41px;top:326px;list-style:none}
.side-nav li{font-size:17px;line-height:25.2px;color:#1a1a1a}
.inquire{left:38px;top:604px;font-size:27px;color:var(--red);letter-spacing:-0.3px}
.address{left:40px;font-family:Arial,sans-serif;font-size:11.6px;line-height:14.5px;color:#111}
.address.first{top:654px}
.address.second{top:712px}

.promo{left:311px;top:293px;width:515px;height:107px;background:var(--black);border-radius:0 0 8px 8px}
.promo-offer{left:319px;top:302px;width:260px;text-align:center;font-family:"Varela Round",sans-serif;
  color:var(--yellow);font-size:31px;line-height:42px}
.promo-day{left:608px;top:297px;font-family:"Varela Round",sans-serif;color:var(--white);font-size:23px;line-height:31.5px}

.card{left:304px;width:532px;height:239px;background:var(--black);border-radius:10px}
.card-inner{left:313px;width:514px;height:221px;background:var(--red-deep);border-radius:8px}
.card.one{top:420px}.card-inner.one{top:429px}
.card.two{top:724px}.card-inner.two{top:733px}

.best-line{left:334px;top:476px;color:var(--white);font-size:36px;letter-spacing:-0.5px}
.best-bold{left:335px;top:517px;color:var(--white);font-family:"Varela Round",sans-serif;font-size:25px}
.best-price{left:338px;top:559px;color:var(--yellow);font-family:"Varela Round",sans-serif;font-size:19.5px}

.photo-woman{left:640px;top:411px;width:210px;height:290px;border-radius:40% 40% 12px 12px;
  background:linear-gradient(180deg,#e9b690 0%,#d99a78 60%,rgba(200,0,0,0) 100%)}
.photo-man{left:291px;top:696px;width:290px;height:346px;border-radius:45% 45% 8px 8px;
  background:linear-gradient(180deg,#d8a07c 0%,#c98d6c 65%,rgba(200,0,0,0) 100%)}

.men-title{left:594px;top:743px;color:var(--white);font-size:25px;letter-spacing:-0.4px}
.men-list{left:619px;top:777px;list-style:none}
.men-list li{font-family:"Varela Round",sans-serif;color:var(--white);font-size:21px;line-height:25.5px}
.other{left:693px;top:926px;display:flex;align-items:center;gap:6px;color:var(--yellow);
  font-family:"Varela Round",sans-serif;font-size:13px}

.footer{left:0;top:1044px;width:858px;height:116px;background:var(--black)}
.footer-links{left:0;top:1065px;width:858px;text-align:center;font-family:Arial,sans-serif;font-size:10.6px;color:var(--white)}
.copyright{left:0;top:1087px;width:858px;text-align:center;font-family:Arial,sans-serif;font-size:9.6px;color:var(--orange)}
.footer-brand{left:0;top:1114px;width:858px;text-align:center;font-family:"Varela Round",sans-serif;font-size:16px;color:#f29b9b}
</style>
</head>
<body>

<div class="abs hero" role="img" aria-label="Photo of a smiling woman with hands raised beside legs in heels on red satin"></div>
<div class="abs hero-band"></div>
<div class="abs brand-tab"><span class="brand-name">Glow on<br>the Avenue</span></div>

<div class="abs side-shadow"></div>
<div class="abs side-panel"></div>
<ul class="abs side-nav">
  <li>Waxing</li><li>City brow bar</li><li>Eyes incl. Lash extensions</li><li>Tanning</li>
  <li>Hands &amp; Feet</li><li>Facial &amp; Massage</li><li>Makeup</li><li>Specials</li>
  <li>Products</li><li>Blog</li>
</ul>
<div class="abs inquire">INQUIRE NOW!</div>
<p class="abs address first">Australia NSW -312<br>Harbour Rd Bayview<br>2260- 02 40011234</p>
<p class="abs address second">Australia NSW -87<br>Harbour Rd Lakeside<br>2270 -02 40015678</p>

<div class="abs promo"></div>
<div class="abs promo-offer">20% OFF<br>ALL WAXING</div>
<div class="abs promo-day">WAX ME<br>WEDNESDAYS<br>Call TODAY!</div>

<div class="abs card one"></div>
<div class="abs card-inner one"></div>
<div class="abs best-line">We are the Best in</div>
<div class="abs best-bold">Wax Down Under</div>
<div class="abs best-price">Brazilians from $39.00</div>
<div class="abs photo-woman" role="img" aria-label="Photo of a seated woman with a flower in her hair beside a straw hat"></div>

<div class="abs card two"></div>
<div class="abs card-inner two"></div>
<div class="abs photo-man" role="img" aria-label="Photo of a shirtless man in sunglasses flexing both arms"></div>
<div class="abs men-title">Specializes in men’s</div>
<ul class="abs men-list">
  <li>Underarms</li><li>Full Arms</li><li>Top Arms</li><li>Chest</li><li>Stomach</li>
</ul>
<div class="abs other">
  <svg width="14" height="10" viewBox="0 0 14 10" aria-hidden="true"><path d="M0 3.5h7V0l7 5-7 5V6.5H0z" fill="#f2e024"/></svg>
  <span>Other Services</span>
</div>

<div class="abs footer"></div>
<div class="abs footer-links">Home | Waxing | City brow bar | Eyes incl. Lash extensions | Tanning | Hands &amp; Feet | Facials &amp; Massage | Makeup | Specials | Products | Blog | Contact Us</div>
<div class="abs copyright">Copyright © 2013 Glow on the Avenue. All Rights Reserved</div>
<div class="abs footer-brand">Glow on the Avenue</div>

</body>
</html>
```